120ml Jar Label — Masculine Cosmetic Foot Balm for Cracked, Hardworking Heels

We need a print-ready wraparound label for a 120ml jar — a brown/amber glass jar with a black metal screw lid (file photo attached).

--DO NOT PUT A BARCODE ON THE LABEL PLEASE--
**PLEASE READ "PLAN HUDDLE PROJECT BRIEF FINAL.MD" IN ATTACHED FILES IF YOU ARE SUBMITTING A DESIGN.**

The label is 190mm wide × 40mm high.
We need files to be in an .ai format with a 2mm bleed at the end.
Social media handle: @bramblekeepnz (facebook, instagram and tiktok)

Bramble Keep is a New Zealand foot-care brand making practical, no-nonsense products for hardworking men whose jobs wreck their feet. Our flagship product, Ridge Mender Balm, helps fix thick, cracked, hardworking skin.

Brand color scheme and overview is all in the brief file. You may add some brand aligned colors outside of the specified hex codes as you see fit to make a great design. Feel free to remove the "Bramble Keep" text from the logo so Bramble Keep is not doubled up on the front of the label

The tone we want: direct, rugged, and credible — like a workwear brand, not a spa brand. Most cracked-heel products on the market lean soft and feminine; we want to stand apart by looking like a serious fix for a real problem, made in New Zealand.

Full legal requirements for New Zealand cosmetic labelling (ingredients, directions, net contents, origin, etc.) are listed in the attached brief document — these are non-negotiable and must stay legible.

Please see the label attached "Label spacing guide" for this project's rough spacing guide. This label is the same size and sits well on the jar. This label doesn't need to be spaced quite as much as the Verin Label

I want to run the design for a week - I feel 7 days is a good amount of time for designers to see the work, digest the brief and create something remarkable and memorable for Bramble Keep.

Target Market(s)

Working men in New Zealand whose jobs or lifestyle put heavy wear on their feet — tradies, farmers, hospital/shift workers, hunters, and outdoors people. Practical, value-driven buyers rather than luxury skincare shoppers.

Industry/Entity Type

Beauty / Health & Wellness / Cosmetics

Font styles to use
Sans Serif
Other font styles liked:
• Montserrat (bold, headings), Inter (regular, body)

Colors
00AB8E
00BBA5
67D7C9
C6EFE9
E9F9F6
FFC000
F8CF3A
FAE287
FDF2CF
FEFAEE

Requirements
Must have
• All NZ cosmetic labelling requirements from the attached brief (product name, tag line, net contents, ingredients, directions, storage, made in NZ) — legible and complete, not omitted for aesthetics Fits 190mm × 40mm wraparound format for a 120ml brown jar with black lid Uses our existing brand colors: Deep Olive #3C4A34, Bone White #F4EFE6, Terracotta Clay #C1683D, and Warm Grey #4A4540 (exact palette in attached brief) Uses Montserrat (headings) and Inter (body) or close equivalents Incorporates our existing shield-and-wing logo (attached) Brand name and product name clearly readable from a normal shelf/bathroom-cabinet distance
Nice to have
• A style that could extend into a hero/product photo later, similar to the NZ-hills-backdrop look on our website (screenshot attached) — not required for the label itself, just good to keep in mind Original icon work (e.g. a small soak/apply/sock icon set) if it fits the rugged brand feel A design that could work as a small back-label/wraparound split if the front can't fit everything at a readable size
Should not have
• No pastel colors, floral motifs, or delicate script fonts — this should never look like spa/luxury skincare. Don't introduce new brand colors outside the palette provided other than black.

```html
<!DOCTYPE html>
<html lang="en">
<head>
<meta charset="utf-8">
<title>Bramble Keep – Ridge Mender Balm wraparound label</title>
<link rel="stylesheet" href="https://fonts.googleapis.com/css2?family=Inter:wght@400;700&family=Montserrat:wght@400;600;700&display=swap">
<style>
  :root {
    --canvas: #e8e8e8;
    --band: #3b342e;
    --panel-dark: #3e3731;
    --bone: #f4efe6;
    --clay: #c1683d;
    --ink: #3a342f;
  }
  * { box-sizing: border-box; margin: 0; padding: 0; }
  html, body { width: 848px; height: 1200px; overflow: hidden; }
  body {
    background: var(--canvas);
    font-family: "Inter", Arial, sans-serif;
    color: var(--ink);
    position: relative;
  }
  .label {
    position: absolute;
    left: 47px; top: 521px;
    width: 754px; height: 158px;
    background: var(--band);
  }
  .panel {
    position: absolute;
    top: 8px; bottom: 8px;
  }
  .panel--info {
    left: 0; width: 251px;
    background: var(--bone);
    padding: 9px 16px 0 16px;
    font-size: 10.6px;
    line-height: 13.4px;
  }
  .panel--front {
    left: 251px; width: 251px;
    background: var(--panel-dark);
  }
  .panel--ingredients {
    left: 502px; width: 252px;
    background: var(--bone);
    padding: 15px 16px 0 14px;
    font-size: 10.6px;
    line-height: 13.4px;
    text-align: justify;
  }
  .info-block { text-align: justify; margin-bottom: 8px; }
  .info-block strong, .panel--ingredients strong { font-weight: 700; }
  .info-foot {
    display: flex; justify-content: space-between; align-items: baseline;
    margin-top: 10px;
  }
  .origin { font-weight: 700; font-size: 10.6px; letter-spacing: -0.1px; }
  .net { font-family: "Montserrat", Arial, sans-serif; font-weight: 600; font-size: 13px; }
  .frame { position: absolute; inset: 0; }
  .brand-tab {
    position: absolute;
    left: 82px; top: 0; width: 86px; height: 89px;
    display: flex; flex-direction: column; align-items: center; justify-content: flex-end;
    padding-bottom: 11px;
  }
  .brand-name {
    font-family: "Montserrat", Arial, sans-serif;
    font-weight: 700;
    color: var(--bone);
    font-size: 10.5px;
    line-height: 11px;
    text-align: center;
    letter-spacing: 0.2px;
  }
  .product-name {
    position: absolute; left: 0; right: 0; top: 94px;
    text-align: center;
    font-family: "Montserrat", Arial, sans-serif;
    font-weight: 700;
    font-size: 14.5px;
    letter-spacing: 0.4px;
    color: var(--clay);
  }
  .tagline {
    position: absolute; left: 0; right: 0; top: 119px;
    text-align: center;
    font-family: "Montserrat", Arial, sans-serif;
    font-weight: 400;
    font-size: 10px;
    letter-spacing: 0.6px;
    color: var(--bone);
  }
</style>
</head>
<body>
  <div class="label">
    <section class="panel panel--info">
      <p class="info-block"><strong>DIRECTIONS:</strong> Apply generously to clean, dry feet, focusing on heels and thick or cracked areas. For cracked heels, wear our moisture-locking socks overnight. Use daily.</p>
      <p class="info-block"><strong>STORAGE:</strong> Keep out of direct sunlight. Best used within six months of opening.</p>
      <div class="info-foot">
        <span class="origin">MADE IN NEW ZEALAND</span>
        <span class="net">120ml</span>
      </div>
    </section>

    <section class="panel panel--front">
      <svg class="frame" width="251" height="142" viewBox="0 0 251 142" aria-hidden="true">
        <path d="M13,5 H82 M168,5 H238 A8,8 0 0 0 246,13 V129 A8,8 0 0 0 238,137 H13 A8,8 0 0 0 5,129 V13 A8,8 0 0 0 13,5"
              fill="none" stroke="#f4efe6" stroke-width="1"/>
        <path d="M17,10 H82 M168,10 H234 A7,7 0 0 0 241,17 V125 A7,7 0 0 0 234,132 H17 A7,7 0 0 0 10,125 V17 A7,7 0 0 0 17,10"
              fill="none" stroke="#c1683d" stroke-width="2"/>
        <path d="M82,0 H168 V81 A8,8 0 0 0 160,89 H90 A8,8 0 0 0 82,81 Z" fill="#c1683d" stroke="#f4efe6" stroke-width="1"/>
        <circle cx="6" cy="5" r="2.5" fill="#c1683d"/>
        <circle cx="245" cy="5" r="2.5" fill="#c1683d"/>
        <circle cx="6" cy="137" r="2.5" fill="#c1683d"/>
        <circle cx="245" cy="137" r="2.5" fill="#c1683d"/>
        <line x1="60" y1="112" x2="191" y2="112" stroke="#f4efe6" stroke-width="0.8"/>
      </svg>
      <div class="brand-tab">
        <span class="brand-name">BRAMBLE<br>KEEP NZ</span>
      </div>
      <h1 class="product-name">RIDGE MENDER BALM</h1>
      <p class="tagline">FOR HARDWORKING SOLES</p>
    </section>

    <section class="panel panel--ingredients">
      <p><strong>INGREDIENTS:</strong> Shea Butter, Beef Tallow, Beeswax, Grape Seed Oil, Vegetable Glycerin, Lanolin, Panthenol, Gluconolactone &amp; Sodium Benzoate, Manuka Honey, Allantoin, Vitamin E, Tea Tree Essential Oil, Lemon Myrtle Essential Oil, Rosemary Oleoresin Extract.</p>
    </section>
  </div>
</body>
</html>
```